[Design ONLY] Design for our Ecommerce business website

We require a web design for our ecommerce business website. We sell textbooks, Computer & Accessories, Gifts and stationery and Laptop/IT support service etc
Requirement:
We Require 3 pages for each design: Homepage, Product page and Payment page
Design Approach:
Design UI to be have a modern and professional feel and user experience must be good.
Responsive web design approach.
1. Home page
- Logo/Heading
- Navigation links to other pages eg. About us
- Appropriate images/banners
- A special offer
- Recent News
Include an overview of the business:
- provide general information
- contact information
- links to social media
- Frequently Asked Questions (FAQ) page
Publish store policies and make sure they are not too difficult to find:
- shipping and return policies
- outline the return process and what products can be returned
- provide easy access to a privacy policy that covers shoppers’ personal and financial information (this is crucial)
2. Product
Product Pages should include:
- Pictures, descriptions, order and price information for your products and/or services.
- Navigation links to other pages, especially home, about us, order and other product pages.
- Links to a shopping cart
- Add to wishlist
- Related or recommend products
3. Payment
- Standard payment form with payment integration with Brenox and Lumbix.
- Shipping or Self Collection fee
User Experience Aspect:
Well-Defined Product Categories
a. The top level of navigation should show the set of categories that the site offers. Group products into categories and subcategories. Category labels work best as single words that describe the range of products, so shoppers can scan through them and instantly understand what they represent.
Product Search
a. Build a search function that helps them easily find what they are looking for.
Make search omnipresent: Put the search box on every page and in familiar locations. The box should be visible, quickly recognizable, and easy to use.
b. Allow sorting and filtering of results: Let shoppers sort search results based on various criteria (best sellers, highest or lowest price, product rating, newest item, etc.) as well as eliminate items that do not fit within a certain category.
Product Quick view
a. A “quick view” reduces the time it takes for shoppers to find the right product by eliminating unnecessary page loads. Also, be sure to include a prominently positioned “Add to Cart” button as well as a “Save to Wishlist” functionality.
b. Show Related and Recommended Products. This can be displayed on a product detail page.
Target Market(s)
university students
Number of Pages Required
3 page
Requirements
Must have
- Note * its a university store. not a normal ecommerce shop*
Do include design for the 3 pages specified. Homepage, product page and payment page.

```html
<!DOCTYPE html>
<html lang="en">
<head>
<meta charset="utf-8">
<title>KAL Coop – Choose Payment Method</title>
<link href="https://fonts.googleapis.com/css2?family=Poppins:wght@400;500;600;700&family=Hind:wght@400;500&display=swap" rel="stylesheet">
<style>
:root{
  --navy:#1b2453;
  --ink:#111;
  --muted:#555;
  --line:#dcdcdc;
  --panel:#f7f7f7;
  --footer:#0d5aa7;
  --white:#fff;
}
*{box-sizing:border-box;margin:0;padding:0}
html,body{width:934px;height:1200px;overflow:hidden;background:var(--white)}
body{position:relative;font-family:'Poppins',sans-serif;color:var(--ink)}
.abs{position:absolute}
.topbar{left:0;top:0;width:934px;height:33px;background:var(--navy);color:var(--white);font-size:9px;font-weight:600}
.topbar span{position:absolute;top:11px}
.topbar .sep{top:10px;width:1px;height:14px;background:var(--white)}
.brand{font-weight:600;font-size:20px;line-height:1;white-space:nowrap}
.brand-mark{width:12px;height:12px}
.search{left:323px;top:54px;width:419px;height:31px;border:1px solid #bbb;font-size:9px;color:#777}
.search .cat{position:absolute;left:0;top:0;width:96px;height:29px;border-right:1px solid #bbb;padding:9px 9px}
.badge{width:13px;height:13px;border-radius:50%;background:var(--navy);color:#fff;font-size:8px;text-align:center;line-height:13px;font-weight:600}
.nav{top:104px;font-size:9.5px;font-weight:500}
.rule{left:0;top:125px;width:934px;height:1px;background:var(--line)}
h1{position:absolute;left:57px;top:139px;font-size:22px;font-weight:700}
.pay{left:45px;top:193px;width:353px;height:401px;background:var(--panel);border:1px solid var(--line);font-family:'Hind',sans-serif;color:#333}
.pay .txt{font-size:12px;line-height:14px}
.radio{width:12px;height:12px;border-radius:50%;border:3px solid #999;background:#fff}
.radio.on{border:3px solid var(--navy)}
.field{border:1px solid #ccc;background:#fff;font-size:13px;color:#bbb;padding:4px 5px;font-family:'Hind',sans-serif}
.label{font-size:10px}
.req{color:#d00}
.summary{font-size:12px}
.summary .v{color:#888;font-weight:600;font-size:11px}
.btn{background:var(--navy);color:#fff;text-align:center}
.box{background:var(--panel);border:1px solid var(--line)}
.box h3{font-size:11.5px;font-weight:600}
.box p{font-size:11.5px;color:#333;line-height:1.22}
.smallbtn{background:var(--navy);color:#fff;font-size:9.5px;height:23px;line-height:23px;text-align:center}
.footer{left:0;top:1028px;width:934px;height:172px;background:var(--footer);color:#fff}
.footer h4{position:absolute;top:36px;font-size:11px;font-weight:600}
.footer p{position:absolute;font-size:10.5px;line-height:1.4;color:#e3ecf7}
</style>
</head>
<body>

<header>
  <div class="abs topbar">
    <svg class="abs" style="left:46px;top:8px" width="16" height="16"><circle cx="8" cy="8" r="7" fill="none" stroke="#fff" stroke-width="1.2"/><text x="8" y="11" font-size="8" fill="#fff" text-anchor="middle">%</text></svg>
    <span style="left:68px">Purchase Offer</span>
    <svg class="abs" style="left:159px;top:9px" width="14" height="14"><path d="M3 2l3 0 1 3-2 1a7 7 0 003 3l1-2 3 1v3c-6 1-10-3-9-9z" fill="none" stroke="#fff" stroke-width="1"/></svg>
    <span style="left:181px">+000 000 0000</span>
    <svg class="abs" style="left:637px;top:11px" width="11" height="11"><circle cx="5.5" cy="5.5" r="4.8" fill="none" stroke="#fff"/><text x="5.5" y="8.5" font-size="7" fill="#fff" text-anchor="middle">?</text></svg>
    <span style="left:652px">Need Help</span>
    <i class="abs sep" style="left:713px"></i>
    <span style="left:727px">My Account</span>
    <i class="abs sep" style="left:797px"></i>
    <span style="left:815px">User Account</span>
  </div>

  <div class="abs brand-mark" style="left:47px;top:64px;background:var(--navy)"></div>
  <div class="abs brand" style="left:64px;top:60px;color:var(--navy)">KAL Coop</div>

  <div class="abs search">
    <div class="cat">All Product <span style="position:absolute;right:7px">⌄</span></div>
    <svg class="abs" style="left:392px;top:8px" width="13" height="13"><circle cx="5.5" cy="5.5" r="4.5" fill="none" stroke="#999" stroke-width="1.2"/><path d="M9 9l3.5 3.5" stroke="#999" stroke-width="1.2"/></svg>
  </div>

  <svg class="abs" style="left:769px;top:61px" width="19" height="19"><path d="M3 8a7 7 0 0113-2M16 11a7 7 0 01-13 2" fill="none" stroke="#111" stroke-width="1.5"/><path d="M16 2v4h-4M3 17v-4h4" fill="none" stroke="#111" stroke-width="1.5"/></svg>
  <svg class="abs" style="left:806px;top:61px" width="20" height="18"><path d="M10 16S2 11 2 6a4 4 0 018-1 4 4 0 018 1c0 5-8 10-8 10z" fill="none" stroke="#111" stroke-width="1.5"/></svg>
  <div class="abs badge" style="left:820px;top:56px">0</div>
  <svg class="abs" style="left:848px;top:60px" width="16" height="20"><rect x="1.5" y="6" width="13" height="13" fill="none" stroke="#111" stroke-width="1.5"/><path d="M5 8V4a3 3 0 016 0v4" fill="none" stroke="#111" stroke-width="1.5"/></svg>
  <div class="abs badge" style="left:861px;top:56px">0</div>

  <nav>
    <span class="abs nav" style="left:46px">Computer &amp; Accessories</span>
    <span class="abs nav" style="left:219px">Memorabilia</span>
    <span class="abs nav" style="left:360px">Books</span>
    <span class="abs nav" style="left:466px">Textbooks</span>
    <span class="abs nav" style="left:586px">Others Servies</span>
    <span class="abs nav" style="left:727px">About Us</span>
    <span class="abs nav" style="left:830px">KAL Coop</span>
  </nav>
  <div class="abs rule"></div>
</header>

<main>
  <h1>Choose Payment Methad</h1>

  <section class="abs pay">
    <div class="abs radio" style="left:16px;top:16px"></div>
    <div class="abs" style="left:45px;top:11px;font-size:15px;font-weight:500;color:var(--navy)">Lumbix</div>
    <div class="abs" style="left:19px;top:32px;width:330px;height:53px;background:#efefef"></div>
    <div class="abs radio on" style="left:16px;top:53px"></div>
    <div class="abs txt" style="left:62px;top:53px">Credit Card (Brenox)</div>
    <div class="abs" style="left:238px;top:50px;width:22px;height:15px;border-radius:3px;background:#e8a33d"></div>
    <div class="abs" style="left:267px;top:49px;width:31px;height:19px;background:#2a6fd1"></div>
    <div class="abs" style="left:301px;top:49px;width:31px;height:19px;background:#1a2a86"></div>

    <div class="abs txt" style="left:36px;top:113px">Pay with your credit card via Brenox.</div>
    <div class="abs radio" style="left:36px;top:146px"></div>
    <div class="abs txt" style="left:57px;top:146px">Card ending in 0005 (expires 12/24)</div>
    <div class="abs radio on" style="left:36px;top:173px"></div>
    <div class="abs txt" style="left:57px;top:173px">Use a new payment method</div>

    <div class="abs label" style="left:36px;top:205px">Card Number <span class="req">*</span></div>
    <div class="abs field" style="left:36px;top:220px;width:296px;height:26px">1234 1234 1234 1234</div>
    <svg class="abs" style="left:305px;top:225px" width="26" height="17"><rect x="1" y="1" width="24" height="15" rx="1" fill="none" stroke="#555" stroke-width="1.3"/><path d="M1 6h24" stroke="#555" stroke-width="2"/><path d="M4 12h6" stroke="#555"/></svg>
    <div class="abs label" style="left:36px;top:263px">Expiry Date <span class="req">*</span></div>
    <div class="abs field" style="left:36px;top:278px;width:139px;height:26px">MM / YY</div>
    <div class="abs label" style="left:193px;top:263px">Card Code (CVC) <span class="req">*</span></div>
    <div class="abs field" style="left:193px;top:278px;width:139px;height:26px">CVC</div>

    <div class="abs" style="left:36px;top:340px;width:11px;height:11px;border:1px solid #aaa;background:#fff;border-radius:2px"></div>
    <div class="abs" style="left:36px;top:335px;width:290px;font-size:12px;line-height:20px;text-indent:18px">Save payment information to my account for future purchases.</div>
  </section>

  <aside class="summary">
    <div class="abs" style="left:634px;top:180px">Product Total</div><div class="abs v" style="left:801px;top:181px">$0.00</div>
    <div class="abs" style="left:635px;top:199px">Sheping</div><div class="abs v" style="left:801px;top:199px">$0.00</div>
    <div class="abs" style="left:635px;top:217px">Tax</div><div class="abs v" style="left:801px;top:216px">$0.00</div>
    <div class="abs" style="left:635px;top:237px;font-weight:700;font-size:11.5px">Total Prize</div>
    <div class="abs" style="left:789px;top:234px;font-weight:700;font-size:15px">$10.98</div>
    <div class="abs btn" style="left:636px;top:274px;width:140px;height:40px;line-height:40px;font-size:17px">Place Order</div>
    <div class="abs" style="left:623px;top:337px;width:252px;height:1px;background:#bbb"></div>
  </aside>

  <section class="abs box" style="left:46px;top:618px;width:577px;height:207px">
    <div class="abs" style="left:192px;top:0;width:1px;height:207px;background:var(--line)"></div>
    <div class="abs" style="left:384px;top:0;width:1px;height:207px;background:var(--line)"></div>
    <h3 class="abs" style="left:16px;top:18px">Billing Adress</h3>
    <p class="abs" style="left:16px;top:66px;width:172px">Veris 41 Str. 18320, Marlow Heights, Eldoria</p>
    <div class="abs smallbtn" style="left:18px;top:143px;width:107px">Edit Billing Adress</div>
    <h3 class="abs" style="left:212px;top:14px">Shipping Adress</h3>
    <p class="abs" style="left:209px;top:63px;width:176px">Halden Works Brightmoor Lane 27 40218 Ostvale</p>
    <div class="abs smallbtn" style="left:214px;top:143px;width:107px">Edit&nbsp; Billing Adress</div>
    <h3 class="abs" style="left:404px;top:14px">Shipping Method</h3>
    <p class="abs" style="left:406px;top:63px;width:150px">Lorem ipsum dolor sit amet, consectetur</p>
    <div class="abs smallbtn" style="left:407px;top:142px;width:107px">Edit Shipping Method</div>
  </section>

  <section class="abs box" style="left:45px;top:838px;width:579px;height:172px">
    <div class="abs" style="left:252px;top:0;width:1px;height:172px;background:var(--line)"></div>
    <div class="abs" style="left:421px;top:0;width:1px;height:172px;background:var(--line)"></div>
    <div class="abs" style="left:501px;top:0;width:1px;height:172px;background:var(--line)"></div>
    <h3 class="abs" style="left:19px;top:7px;font-weight:500">Orbex Notebook Pro</h3>
    <div class="abs" role="img" aria-label="Laptop product photo" style="left:18px;top:55px;width:51px;height:35px;background:linear-gradient(135deg,#3b4a5c,#7f95ad 55%,#222)"></div>
    <p class="abs" style="left:83px;top:50px;width:155px">Lorem ipsum dolor sit amet, consectetur adipi-scing elit, sed do eiusmod tempor incididunt ut</p>
    <div class="abs smallbtn" style="left:22px;top:125px;width:78px;height:20px;line-height:20px;font-size:10.5px">Edit Cart</div>
    <h3 class="abs" style="left:293px;top:7px">Delivery Estimate</h3>
    <p class="abs" style="left:293px;top:67px;width:115px">Lorem ipsum dolor sit amet, consec</p>
    <h3 class="abs" style="left:448px;top:7px">Qty</h3>
    <p class="abs" style="left:457px;top:76px">1</p>
    <h3 class="abs" style="left:523px;top:9px">Price</h3>
    <p class="abs" style="left:526px;top:76px">$3.99</p>
  </section>
</main>

<footer class="abs footer">
  <div class="abs brand-mark" style="left:56px;top:44px;background:#fff"></div>
  <div class="abs brand" style="left:73px;top:40px;color:#fff">KAL Coop</div>
  <p style="left:56px;top:80px;width:205px">Lorem ipsum dolor sit amet, consec tetur adipiscing elit, sed do eiusmod tempor incididunt ut labore et dolo.</p>

  <h4 style="left:317px">CONNECT PEOPLE</h4>
  <p style="left:312px;top:62px;width:140px">Connect with us and stay in the loop.</p>
  <svg class="abs" style="left:314px;top:110px" width="130" height="16"><circle cx="7" cy="8" r="6" fill="#8fb3dc"/><circle cx="43" cy="8" r="6" fill="#fff"/><rect x="71" y="2" width="18" height="13" rx="4" fill="#8fb3dc"/><rect x="109" y="2" width="13" height="13" rx="3" fill="none" stroke="#8fb3dc" stroke-width="2"/></svg>

  <h4 style="left:531px">EMAIL UPDATES</h4>
  <p style="left:531px;top:62px;width:160px">Be the first to hear about our Event announcements.</p>
  <div class="abs" style="left:530px;top:104px;width:170px;height:30px;background:#fff;border-radius:2px;color:#777;font-size:9px;padding:9px 12px;font-weight:400">Enter your email id</div>
  <svg class="abs" style="left:668px;top:111px" width="17" height="16"><path d="M1 8L16 1 12 15 8 10zM8 10l8-9" fill="var(--navy)" stroke="var(--navy)" stroke-linejoin="round"/></svg>

  <h4 style="left:773px">CONTACT US</h4>
  <p style="left:772px;top:62px;width:120px">Question? We've got answer. Try us.</p>
  <div class="abs" style="left:772px;top:104px;width:97px;height:29px;background:#fff;border:1px solid #333;color:#111;font-size:8.5px;text-align:center;line-height:27px;letter-spacing:1px">EMAIL US</div>

  <div class="abs" style="left:906px;top:48px;width:28px;height:56px;background:var(--navy)"></div>
  <svg class="abs" style="left:913px;top:56px" width="14" height="12"><path d="M1 1h12v8H5l-3 2V9H1z" fill="#fff"/></svg>
  <svg class="abs" style="left:912px;top:84px" width="16" height="11"><rect x="0.5" y="0.5" width="15" height="10" fill="#fff"/><path d="M1 1l7 5 7-5" fill="none" stroke="var(--navy)"/></svg>
</footer>

</body>
</html>
```